Looking to Rebrand landscaping business

Hello, Im looking for a flyer to be created. Basically something clean that gets the point across. These flyers will be distributed door to door throughout the community. I want a design that is simple to read and allows the eye to flow along through it, nothing crammed.
Here is a design i love. http://www.pixelbazaar.example/design/4839215
Services we offer:
Lawn Maintenance
Landscaping Services
Aeration
Thatch Removal
Fertilizer & Weed Control Applications (Programs Available)
Spring & Fall Clean ups
New Lawn Installations
Pruning
Mulch and rock Installation
Hedge Trimming
Winter Snow Removal Services
& more
Would like to have a special of:
Let us earn your Business
call now and get your first cut free of charge.
*conditions apply
Other points which COULD be included
Free Estimates
Fully Insured
Email: ADMIN@OAKVALEYARDWORKS.CA
PHONE: 555-384-9027
Serving Saint John & Surrounding Areas
I will be rebranding the complete business and interested in having more work done in the future.
Landscaping

```html
<!DOCTYPE html>
<html lang="en">
<head>
<meta charset="utf-8">
<title>Oakvale – A Service For Every Season</title>
<link rel="stylesheet" href="https://fonts.googleapis.com/css2?family=Raleway:wght@400;500;600;700;800&display=swap">
<style>
  :root {
    --green: #3aa935;
    --green-dark: #2f9a34;
    --green-light: #8dc63f;
    --green-pale: #c9e6a8;
    --text-green: #2a8f36;
    --grey: #6b6b6b;
    --yellow: #eef25a;
    --white: #ffffff;
  }
  * { margin: 0; padding: 0; box-sizing: border-box; }
  html, body { width: 848px; height: 1200px; overflow: hidden; background: var(--white); }
  body { font-family: "Raleway", Arial, sans-serif; }
  .flyer { position: relative; width: 848px; height: 1200px; overflow: hidden; background: var(--white); }

  .hero { position: absolute; left: 0; top: 0; width: 848px; height: 560px; }

  .services { position: absolute; left: 46px; top: 548px; }
  .services-title { font-size: 26px; font-weight: 600; color: var(--grey); margin-bottom: 12px; }
  .service-list { list-style: none; }
  .service-item {
    display: flex; align-items: flex-start; gap: 14px;
    font-size: 18.5px; font-weight: 600; color: var(--text-green);
    line-height: 24px; margin-bottom: 11px;
  }
  .service-item .tick { flex: none; width: 26px; height: 26px; margin-top: -2px; }
  .service-item.two-line { margin-bottom: 11px; }

  .badge-promise {
    position: absolute; left: 530px; top: 625px; width: 242px; height: 178px;
    background: var(--green-light);
    border-radius: 14px 95px 14px 95px;
    border: 3px solid var(--white);
    box-shadow: 0 4px 10px rgba(0,0,0,.18);
    color: var(--white); font-size: 25px; font-weight: 600; line-height: 40px;
    padding: 24px 0 0 20px;
  }
  .badge-offer {
    position: absolute; left: 504px; top: 740px; width: 200px; height: 246px;
    background: var(--green);
    border-radius: 18px 70px 100px 18px;
    border: 4px solid var(--white);
    box-shadow: 0 4px 12px rgba(0,0,0,.25);
    padding: 20px 0 0 14px; color: var(--white);
  }
  .offer-headline { font-size: 22px; font-weight: 700; line-height: 27px; margin-bottom: 14px; }
  .offer-body { font-size: 21px; font-weight: 400; line-height: 27px; color: var(--yellow); }
  .offer-body strong { font-weight: 700; }
  .offer-note { font-size: 10px; color: var(--yellow); margin-top: 6px; margin-left: 16px; }

  .footer {
    position: absolute; left: 0; top: 1072px; width: 848px; height: 128px;
    background: linear-gradient(180deg, #a4d44a 0%, var(--green-light) 100%);
  }
  .service-area { position: absolute; left: 30px; top: 34px; font-size: 20px; font-weight: 500; color: var(--green-pale); }
  .contact { position: absolute; top: 78px; display: flex; align-items: center; gap: 10px; font-size: 28px; font-weight: 400; color: var(--white); }
  .contact-email { left: 30px; }
  .contact-phone { left: 548px; }
  .contact svg { width: 30px; height: 30px; }

  .brand-box {
    position: absolute; left: 513px; top: 1040px; width: 288px; height: 89px;
    background: var(--white); box-shadow: 0 3px 8px rgba(0,0,0,.25);
    display: flex; align-items: center; justify-content: center;
  }
  .brand-name { font-size: 46px; font-weight: 400; color: var(--green); letter-spacing: 1px; }
</style>
</head>
<body>
<main class="flyer">
  <svg class="hero" viewBox="0 0 848 560" xmlns="http://www.w3.org/2000/svg">
    <defs>
      <linearGradient id="photoTone" x1="0" y1="0" x2="0" y2="1">
        <stop offset="0" stop-color="#5aa4e6"/>
        <stop offset="0.45" stop-color="#c9d7e2"/>
        <stop offset="0.7" stop-color="#4f8a2c"/>
        <stop offset="1" stop-color="#3c7a22"/>
      </linearGradient>
      <path id="bannerLine" d="M40 420 Q380 520 720 448"/>
    </defs>
    <rect class="hero-photo" role="img" aria-label="Photo of a large white house with a landscaped lawn, shrubs and a stone path" x="0" y="0" width="848" height="520" fill="url(#photoTone)"/>
    <path class="banner-band" d="M0 349 Q420 500 848 385 L848 442 Q420 560 0 413 Z" fill="var(--green)"/>
    <path class="banner-edge" d="M0 413 Q420 560 848 442 L848 560 L0 560 Z" fill="var(--white)"/>
    <path class="banner-accent" d="M0 421 Q420 568 848 452" fill="none" stroke="var(--green-light)" stroke-width="6"/>
    <text font-family="Raleway, Arial, sans-serif" font-size="42" fill="#ffffff" letter-spacing="1">
      <textPath href="#bannerLine">A <tspan font-weight="800">SERVICE</tspan> FOR EVERY <tspan font-weight="800">SEASON</tspan></textPath>
    </text>
  </svg>

  <section class="services">
    <h2 class="services-title">Services we offer</h2>
    <ul class="service-list">
      <li class="service-item"><svg class="tick" viewBox="0 0 26 26"><rect x="1" y="5" width="19" height="19" rx="3" fill="var(--green)"/><path d="M6 14 L11 19 L24 3" fill="none" stroke="#fff" stroke-width="6"/><path d="M6 14 L11 19 L24 3" fill="none" stroke="var(--green)" stroke-width="3"/></svg>Lawn Maintenance</li>
      <li class="service-item"><svg class="tick" viewBox="0 0 26 26"><rect x="1" y="5" width="19" height="19" rx="3" fill="var(--green)"/><path d="M6 14 L11 19 L24 3" fill="none" stroke="#fff" stroke-width="6"/><path d="M6 14 L11 19 L24 3" fill="none" stroke="var(--green)" stroke-width="3"/></svg>Landscaping Services</li>
      <li class="service-item"><svg class="tick" viewBox="0 0 26 26"><rect x="1" y="5" width="19" height="19" rx="3" fill="var(--green)"/><path d="M6 14 L11 19 L24 3" fill="none" stroke="#fff" stroke-width="6"/><path d="M6 14 L11 19 L24 3" fill="none" stroke="var(--green)" stroke-width="3"/></svg>Aeration</li>
      <li class="service-item"><svg class="tick" viewBox="0 0 26 26"><rect x="1" y="5" width="19" height="19" rx="3" fill="var(--green)"/><path d="M6 14 L11 19 L24 3" fill="none" stroke="#fff" stroke-width="6"/><path d="M6 14 L11 19 L24 3" fill="none" stroke="var(--green)" stroke-width="3"/></svg>Thatch Removal</li>
      <li class="service-item two-line"><svg class="tick" viewBox="0 0 26 26"><rect x="1" y="5" width="19" height="19" rx="3" fill="var(--green)"/><path d="M6 14 L11 19 L24 3" fill="none" stroke="#fff" stroke-width="6"/><path d="M6 14 L11 19 L24 3" fill="none" stroke="var(--green)" stroke-width="3"/></svg><span>Fertilizer &amp; Weed Control Applications<br>(Programs Available)</span></li>
      <li class="service-item"><svg class="tick" viewBox="0 0 26 26"><rect x="1" y="5" width="19" height="19" rx="3" fill="var(--green)"/><path d="M6 14 L11 19 L24 3" fill="none" stroke="#fff" stroke-width="6"/><path d="M6 14 L11 19 L24 3" fill="none" stroke="var(--green)" stroke-width="3"/></svg>Spring &amp; Fall Clean ups</li>
      <li class="service-item"><svg class="tick" viewBox="0 0 26 26"><rect x="1" y="5" width="19" height="19" rx="3" fill="var(--green)"/><path d="M6 14 L11 19 L24 3" fill="none" stroke="#fff" stroke-width="6"/><path d="M6 14 L11 19 L24 3" fill="none" stroke="var(--green)" stroke-width="3"/></svg>New Lawn Installations</li>
      <li class="service-item"><svg class="tick" viewBox="0 0 26 26"><rect x="1" y="5" width="19" height="19" rx="3" fill="var(--green)"/><path d="M6 14 L11 19 L24 3" fill="none" stroke="#fff" stroke-width="6"/><path d="M6 14 L11 19 L24 3" fill="none" stroke="var(--green)" stroke-width="3"/></svg>Pruning</li>
      <li class="service-item"><svg class="tick" viewBox="0 0 26 26"><rect x="1" y="5" width="19" height="19" rx="3" fill="var(--green)"/><path d="M6 14 L11 19 L24 3" fill="none" stroke="#fff" stroke-width="6"/><path d="M6 14 L11 19 L24 3" fill="none" stroke="var(--green)" stroke-width="3"/></svg>Mulch and rock Installation</li>
      <li class="service-item"><svg class="tick" viewBox="0 0 26 26"><rect x="1" y="5" width="19" height="19" rx="3" fill="var(--green)"/><path d="M6 14 L11 19 L24 3" fill="none" stroke="#fff" stroke-width="6"/><path d="M6 14 L11 19 L24 3" fill="none" stroke="var(--green)" stroke-width="3"/></svg>Hedge Trimming</li>
      <li class="service-item"><svg class="tick" viewBox="0 0 26 26"><rect x="1" y="5" width="19" height="19" rx="3" fill="var(--green)"/><path d="M6 14 L11 19 L24 3" fill="none" stroke="#fff" stroke-width="6"/><path d="M6 14 L11 19 L24 3" fill="none" stroke="var(--green)" stroke-width="3"/></svg>Winter Snow Removal Services</li>
      <li class="service-item"><svg class="tick" viewBox="0 0 26 26"><rect x="1" y="5" width="19" height="19" rx="3" fill="var(--green)"/><path d="M6 14 L11 19 L24 3" fill="none" stroke="#fff" stroke-width="6"/><path d="M6 14 L11 19 L24 3" fill="none" stroke="var(--green)" stroke-width="3"/></svg>&amp; MORE</li>
    </ul>
  </section>

  <div class="badge-promise">Free Estimates<br>Fully Insured</div>

  <div class="badge-offer">
    <p class="offer-headline">Let us earn<br>your Business!</p>
    <p class="offer-body">Call now and get<br>your first cut<br><strong>free* of charge</strong>.</p>
    <p class="offer-note">*conditions apply</p>
  </div>

  <footer class="footer">
    <p class="service-area">Serving Saint John &amp; Surrounding Areas</p>
    <p class="contact contact-email">
      <svg viewBox="0 0 30 30"><rect x="2" y="6" width="26" height="18" rx="2" fill="none" stroke="#fff" stroke-width="2.5"/><path d="M3 8 L15 17 L27 8" fill="none" stroke="#fff" stroke-width="2.5"/></svg>
      admin@oakvaleyardworks.ca
    </p>
    <p class="contact contact-phone">
      <svg viewBox="0 0 30 30"><rect x="2" y="2" width="26" height="26" rx="6" fill="#fff"/><path d="M10 7 L13 7 L14 11 L12 13 Q14 17 17 18 L19 16 L23 17 L23 20 Q22 23 19 23 Q9 21 7 11 Q7 8 10 7 Z" fill="var(--green-light)"/></svg>
      555-384-9027
    </p>
  </footer>

  <div class="brand-box"><span class="brand-name">oakvale</span></div>
</main>
</body>
</html>
```